Now Leasing Banner

Looking for a banner that says the following information approx 4' x 30'

Now Leasing Maplewood Terrace 925-318-6054

Target Market(s)

Drive by traffic

Industry/Entity Type

Residential property management

Requirements
Must have
• Clear and readable from a distance

```html
<!DOCTYPE html>
<html lang="en">
<head>
<meta charset="UTF-8">
<title>Now Leasing – Maplewood Terrace</title>
<link rel="stylesheet" href="https://fonts.googleapis.com/css2?family=Oswald:wght@700&display=swap">
<style>
  :root {
    --banner-bg: #1b1b1b;
    --headline-white: #ffffff;
    --phone-yellow: #e4ff00;
    --text-shadow: rgba(0, 0, 0, 0.55);
    --sky-tone: #8a9098;
    --hill-tone: #5b7a3a;
    --town-tone: #6d6a60;
  }
  html, body {
    margin: 0;
    padding: 0;
    overflow: hidden;
    background: var(--banner-bg);
  }
  .banner {
    position: relative;
    width: 1200px;
    height: 160px;
    overflow: hidden;
    background: var(--banner-bg);
    font-family: "Oswald", "Arial Narrow", sans-serif;
    font-weight: 700;
  }
  .aerial-photo {
    position: absolute;
    left: 377px;
    top: -116px;
    width: 392px;
    height: 392px;
    border-radius: 50%;
    background:
      linear-gradient(rgba(0,0,0,0.28), rgba(0,0,0,0.28)),
      linear-gradient(180deg,
        var(--sky-tone) 0%,
        var(--sky-tone) 33%,
        var(--town-tone) 37%,
        var(--hill-tone) 50%,
        var(--hill-tone) 62%,
        var(--town-tone) 78%,
        #4f5a42 100%);
  }
  .headline {
    position: absolute;
    inset: 0;
    display: flex;
    align-items: center;
    justify-content: center;
    gap: 22px;
    margin: 0;
    padding: 0 0 8px;
    font-size: 57px;
    font-weight: 700;
    line-height: 1;
    letter-spacing: 0.4px;
    white-space: nowrap;
  }
  .headline span {
    text-shadow: 2px 3px 4px var(--text-shadow);
  }
  .now-leasing,
  .property-name { color: var(--headline-white); }
  .leasing-phone { color: var(--phone-yellow); }
</style>
</head>
<body>
  <div class="banner">
    <div class="aerial-photo" role="img" aria-label="Aerial view of the apartment community, green hills and surrounding neighborhood"></div>
    <h1 class="headline">
      <span class="now-leasing">Now Leasing</span>
      <span class="property-name">Maplewood Terrace</span>
      <span class="leasing-phone">925-318-6054</span>
    </h1>
  </div>
</body>
</html>
```